Copper Ridge Inquiries Letterhead

I would like to design a letterhead for a private investigation company. Our primary clients will be law firms. The business card is included below

```html
<!DOCTYPE html>
<html lang="en">
<head>
<meta charset="utf-8">
<title>Copper Ridge Inquiries Letterhead</title>
<link href="https://fonts.googleapis.com/css2?family=Roboto:wght@400;500;700&display=swap" rel="stylesheet">
<style>
  :root {
    --navy: #1b3264;
    --orange: #f15a2b;
    --paper: #ffffff;
    --backdrop: #8c8c8c;
  }
  * { box-sizing: border-box; margin: 0; padding: 0; }
  html, body {
    width: 1200px; height: 686px; overflow: hidden;
    background: var(--backdrop);
    font-family: "Roboto", Arial, sans-serif;
  }
  .letterhead {
    position: absolute; left: 348px; top: 18px;
    width: 504px; height: 650px;
    background: var(--paper);
    box-shadow: 0 4px 14px rgba(0,0,0,.25);
    overflow: hidden;
  }
  .rule { position: absolute; left: 0; right: 0; height: 1.5px; background: var(--navy); }
  .rule .accent { position: absolute; left: 25%; width: 50%; top: -0.5px; height: 2.5px; background: var(--orange); }
  .header-rule { top: 58px; }
  .footer-rule { top: 560px; }
  .brand {
    position: absolute; left: 50%; transform: translate(-50%, -50%);
    background: var(--paper); padding: 4px 12px;
    display: flex; align-items: center; gap: 7px;
    color: var(--navy); font-weight: 700; white-space: nowrap;
  }
  .brand-header { top: 58px; font-size: 17px; letter-spacing: .5px; }
  .brand-mark { width: 14px; height: 14px; border-radius: 50%; background: var(--orange); }
  .brand-footer { top: 560px; padding: 3px 6px; }
  .brand-footer .brand-mark { width: 12px; height: 12px; }
  .contact {
    position: absolute; display: flex; align-items: center; gap: 5px;
    font-size: 10.5px; color: var(--navy); white-space: nowrap;
  }
  .contact svg { width: 10px; height: 10px; fill: var(--orange); flex: none; }
  .contact-phone { left: 28px; top: 576px; }
  .contact-license { left: 50%; transform: translateX(-50%); top: 576px; }
  .contact-address { right: 28px; top: 576px; }
  .contact-email { left: 50%; transform: translateX(-50%); top: 596px; }
  .tagline {
    position: absolute; left: 0; right: 0; top: 616px; text-align: center;
    font-size: 10px; color: var(--orange); letter-spacing: .4px; text-transform: uppercase;
  }
  .base-bands { position: absolute; left: 0; bottom: 0; width: 504px; height: 12px; }
</style>
</head>
<body>
  <main class="letterhead">
    <div class="rule header-rule"><span class="accent"></span></div>
    <div class="brand brand-header"><span class="brand-mark"></span>Copper Ridge Inquiries</div>

    <div class="rule footer-rule"><span class="accent"></span></div>
    <div class="brand brand-footer"><span class="brand-mark"></span></div>

    <div class="contact contact-phone">
      <svg viewBox="0 0 24 24"><path d="M6.6 10.8a15 15 0 0 0 6.6 6.6l2.2-2.2c.3-.3.7-.4 1-.2 1.1.4 2.3.6 3.6.6.6 0 1 .4 1 1V20c0 .6-.4 1-1 1A17 17 0 0 1 3 4c0-.6.4-1 1-1h3.5c.6 0 1 .4 1 1 0 1.3.2 2.5.6 3.6.1.3 0 .7-.2 1z"/></svg>
      555.014.2290
    </div>
    <div class="contact contact-license">
      <svg viewBox="0 0 24 24"><path d="M3 5h18v14H3zM5 7v10h14V7zm2 2h5v2H7zm0 4h8v2H7z"/></svg>
      License NO. 04718263
    </div>
    <div class="contact contact-address">
      <svg viewBox="0 0 24 24"><path d="M12 2a7 7 0 0 0-7 7c0 5 7 13 7 13s7-8 7-13a7 7 0 0 0-7-7zm0 9.5A2.5 2.5 0 1 1 12 6.5a2.5 2.5 0 0 1 0 5z"/></svg>
      Fort Calder, TX
    </div>
    <div class="contact contact-email">
      <svg viewBox="0 0 24 24"><path d="M2 5h20v14H2zm2 2v.5l8 5 8-5V7zm0 2.9V17h16V9.9l-8 5z"/></svg>
      daniel@copperridgeinquiries.com
    </div>
    <p class="tagline">Over 20 years of investigative experience</p>

    <svg class="base-bands" viewBox="0 0 504 12" preserveAspectRatio="none" aria-hidden="true">
      <polygon points="0,0 216,0 224,12 0,12" fill="var(--orange)"/>
      <polygon points="232,0 504,0 504,12 240,12" fill="var(--navy)"/>
    </svg>
  </main>
</body>
</html>
```